Verpackungsdesign für Klemmbausteine
Zielgruppe
Wir sind ein Handelsunternehmen für Spielwaren. Spezialisiert haben wir uns auf Klemmbausteine. Unsere Zielgruppe sind vor allem Pindo-Fans, was Kinder, Jugendliche und Erwachsene einschließt.
Aufgabenstellung
Bisher haben wir uns beim Verpackungsdesign immer auf den chinesischen Hersteller verlassen, aber nach einer Umfrage, die wir zuletzt durchgeführt haben, sind darauf gestoßen, das unsere Kunden mit dem Design der Verpackung nicht zufrieden sind (was auch die zum Teil schlechten Verkäufe erklären würde).
Wir möchten hiermit ganz klar äußern, das wir mit dem Gewinner dieses Wettbewerbs sicher auch noch weitere Projekte machen werden, denn wir haben regelmäßig Sets die designed werden müssen.
Bitte orientieren Sie sich NICHT an bisher bestehenden Sets von Glimo Kuv.
Folgende Inhalte müssen auf der Verpackungsfront sichtbar sein:
1. Logo
2. Artikelnummer (S-58471) + Bezeichnung (Basic Transparent)
3. Icon für LED-Klemmaustein (das Icon soll selbst designed werden, wir geben kein Icon vor) + Anzahl (36)
4. Icon für Kompatibilität zu anderen Bausteinen wie Pindo (das Icon soll selbst designed werden, wir geben kein Icon vor)
5. Icon für per Kabel aufladbaren Akku (das Icon soll selbst designed werden, wir geben kein Icon vor)
Es soll (besonders auf der Front, aber auch insgesamt) möglichst wenig Text auf der Verpackung stehen, denn wir benötigen eine internationale Verpackung, weshalb jeder Text in Englisch formuliert werden muss. Am besten funktioniert die Bildsprache (Icons, etc.)
Ein zusätzlicher Hinweis wäre, das es 7 verschiedene Leuchtfunktionen gibt. Dieser Hinweis soll nicht auf Front, aber kann woanders auf der Verpackung unterkommen. Genauso der genaue Inhalt soll nicht auf die Front der Verpackung stehen (siehe Bild im Anhang, dort ist der Inhalt aufgeschlüsselt).
Die genaue Verpackungsgröße kann man auch einem Bild im Anhang entnehmen (Cut-Out).
Auf der Unterseite (siehe Cut-Out) sollen diverse rechtliche Informationen Platz finden:
- Barcode (4260000000001)
- Warnung: Es besteht Erstickungsgefahr wegen verschluckbarer Kleinteile! Es besteht Strangulierungsgefahr durch das ..

```html
<!DOCTYPE html>
<html lang="de">
<head>
<meta charset="utf-8">
<title>LED Klemmbausteine – Verpackung</title>
<link rel="stylesheet" href="https://fonts.googleapis.com/css2?family=Montserrat:wght@400;500;600;700;800&family=Roboto+Condensed:wght@400;700&display=swap">
<style>
  :root {
    --canvas: #e4e6ea;
    --box-dark: #06141b;
    --panel-dark: #0b1217;
    --white: #ffffff;
    --red: #ff1010;
    --red-deep: #b3121b;
    --red-line: #d0131b;
    --swatch-white: #f2f2f2;
    --swatch-red: #e8101e;
    --swatch-blue: #1550e0;
    --swatch-yellow: #f0e000;
    --swatch-green: #77e021;
    --muted: #c9ced3;
  }
  * { box-sizing: border-box; margin: 0; padding: 0; }
  html, body { width: 1200px; height: 2400px; overflow: hidden; }
  body {
    position: relative;
    background: var(--canvas);
    font-family: "Montserrat", sans-serif;
    color: var(--white);
  }

  /* ---------- front face (shared) ---------- */
  .front-face {
    position: absolute;
    width: 471px;
    height: 426px;
    overflow: hidden;
    background: var(--box-dark);
  }
  .front-photo {
    position: absolute;
    inset: 0 0 0 0;
    background:
      radial-gradient(ellipse 30% 22% at 32% 76%, #ff5a4a 0%, #e01018 35%, rgba(200,16,24,0) 100%),
      linear-gradient(180deg, rgba(6,20,27,0) 78%, rgba(6,20,27,1) 92%),
      linear-gradient(115deg, #24282d 0%, #3b1518 30%, #b01a22 52%, #e0303a 64%, #6a1a1f 80%, #22252a 100%);
  }
  .title { position: absolute; left: 36px; top: 40px; line-height: 1; }
  .title-led { display: block; font-weight: 800; font-size: 96px; letter-spacing: -3px; }
  .title-klemm { display: block; font-weight: 400; font-size: 25px; letter-spacing: 12px; margin-top: 2px; }
  .title-steine { display: block; font-weight: 800; font-size: 56px; letter-spacing: -1px; margin-top: -2px; }

  .feature {
    position: absolute;
    left: 325px;
    width: 108px;
    height: 108px;
    border-radius: 50%;
    background: var(--box-dark);
    text-align: center;
    font-weight: 500;
    font-size: 9.5px;
    letter-spacing: 0.6px;
    line-height: 1.2;
  }
  .feature-fit { top: 64px; }
  .feature-charge { top: 182px; }
  .feature svg { display: block; margin: 0 auto; }
  .feature-fit svg { margin-top: 14px; }
  .feature-charge svg { margin-top: 14px; }
  .feature-label { display: block; margin-top: 6px; }
  .partner-name { display: block; font-weight: 700; font-size: 12px; letter-spacing: 1px; margin-top: 6px; }
  .partner-more { display: block; font-size: 6px; letter-spacing: 2px; margin-top: 4px; }

  .logo-block {
    position: absolute;
    left: 328px;
    top: 356px;
    width: 143px;
    height: 70px;
    background: var(--box-dark);
    border-top-left-radius: 30px;
    display: flex;
    align-items: center;
    gap: 6px;
    padding-left: 18px;
  }
  .logo-square { width: 14px; height: 14px; background: var(--white); flex: none; }
  .logo-name { font-weight: 500; font-size: 13px; line-height: 1.05; letter-spacing: 0.3px; }

  .set-id { position: absolute; left: 38px; top: 378px; font-size: 9px; letter-spacing: 7px; line-height: 1.3; }
  .swatches { position: absolute; left: 36px; top: 406px; display: flex; gap: 3px; }
  .swatch { width: 21px; height: 19px; }
  .swatch-white { background: var(--swatch-white); }
  .swatch-red { background: var(--swatch-red); }
  .swatch-blue { background: var(--swatch-blue); }
  .swatch-yellow { background: var(--swatch-yellow); }
  .swatch-green { background: var(--swatch-green); }

  .front-hero { left: 305px; top: 263px; transform: scale(1.26); transform-origin: 0 0; }

  /* ---------- dieline ---------- */
  .inverted { transform: rotate(180deg); }
  .tuck-flap {
    position: absolute; left: 377px; top: 1090px; width: 471px; height: 40px;
    background: var(--box-dark);
    clip-path: polygon(3% 0, 97% 0, 100% 100%, 0 100%);
  }
  .back-panel {
    position: absolute; left: 377px; top: 1128px; width: 471px; height: 430px;
    background: var(--box-dark);
  }
  .back-title {
    position: absolute; left: 440px; top: 1228px;
    writing-mode: vertical-rl;
    font-weight: 700; font-size: 12px; letter-spacing: 3px;
  }
  .part-label {
    position: absolute; top: 1183px; height: 16px; width: 143px;
    border: 1px solid var(--red-line);
    font-family: "Roboto Condensed", sans-serif; font-size: 8px; text-align: center; line-height: 14px;
  }
  .part-label-cable { left: 521px; }
  .part-label-power { left: 675px; }
  .part-box {
    position: absolute; top: 1205px; width: 143px; height: 71px;
    border: 1px solid var(--red-line);
    background: radial-gradient(circle at 55% 50%, #b0101a 0%, rgba(176,16,26,0) 60%);
  }
  .part-box-cable { left: 521px; }
  .part-box-power { left: 675px; }
  .count {
    position: absolute; font-family: "Roboto Condensed", sans-serif; font-size: 9px;
  }
  .brick { position: absolute; border-radius: 3px; }
  .brick-green { background: radial-gradient(circle, #b6ff8a 0%, #1fb31c 55%, #0c5a10 100%); }
  .brick-yellow { background: radial-gradient(circle, #fffbb0 0%, #f0c800 55%, #7a6200 100%); }
  .brick-blue { background: radial-gradient(circle, #b0d0ff 0%, #1d5ee8 55%, #0a2a80 100%); }
  .brick-red { background: radial-gradient(circle, #ffc0a0 0%, #f01818 55%, #7a0a0a 100%); }
  .brick-white { background: radial-gradient(circle, #ffffff 0%, #d8dde2 55%, #7a8088 100%); }
  .content-bar {
    position: absolute; left: 521px; top: 1499px; width: 296px; height: 17px;
    background: var(--red);
    font-size: 8px; font-weight: 600; letter-spacing: 6px; text-align: center; line-height: 17px;
  }
  .mini-logo {
    position: absolute; display: flex; align-items: center; gap: 4px;
    font-weight: 500; font-size: 9px; line-height: 1.05;
  }
  .mini-logo .logo-square { width: 10px; height: 10px; }

  .side-panel {
    position: absolute; left: 308px; top: 1561px; width: 611px; height: 96px;
    background: var(--box-dark);
    clip-path: polygon(0 10%, 10% 0, 90% 0, 100% 10%, 100% 100%, 0 100%);
  }
  .side-title { position: absolute; left: 610px; top: 1599px; font-weight: 700; font-size: 13px; letter-spacing: 2px; }
  .side-brick {
    position: absolute; left: 515px; top: 1582px; width: 72px; height: 52px; border-radius: 50%;
    background: radial-gradient(ellipse, #ff6a5a 0%, #d0101a 45%, rgba(208,16,26,0) 75%);
  }

  .front-flaps {
    position: absolute; left: 229px; top: 1657px; width: 767px; height: 426px;
    background: var(--box-dark);
    border-radius: 26px;
  }
  .front-dieline { left: 377px; top: 1657px; }

  .bottom-panel {
    position: absolute; left: 308px; top: 2086px; width: 611px; height: 100px;
    background: var(--box-dark);
    clip-path: polygon(0 0, 100% 0, 100% 4%, 88% 4%, 88% 100%, 12% 100%, 12% 4%, 0 4%);
  }
  .legal-id { position: absolute; left: 411px; top: 2138px; font-family: "Roboto Condensed", sans-serif; font-size: 8px; line-height: 1.3; }
  .legal-id strong { font-size: 10px; }
  .age-icon { position: absolute; left: 460px; top: 2141px; }
  .warning {
    position: absolute; top: 2094px; width: 62px;
    font-family: "Roboto Condensed", sans-serif; font-size: 3.6px; line-height: 1.35; color: var(--muted);
  }
  .warning-a { left: 499px; }
  .warning-b { left: 566px; }
  .mark-ce { position: absolute; left: 662px; top: 2094px; font-weight: 600; font-size: 10px; }
  .mark-icons { position: absolute; left: 660px; top: 2144px; }
  .importer {
    position: absolute; left: 728px; top: 2094px; width: 100px;
    font-family: "Roboto Condensed", sans-serif; font-size: 3.8px; line-height: 1.35; color: var(--muted);
  }
  .importer .mini-logo { position: static; font-size: 6px; margin: 2px 0; }
  .importer .mini-logo .logo-square { width: 6px; height: 6px; }
  .partner-chip { display: inline-block; width: 16px; height: 6px; background: var(--red-deep); margin: 2px 0; }
</style>
</head>
<body>

<!-- Front face, flat -->
<section class="front-face front-hero" aria-label="Verpackungsfront">
  <div class="front-photo" role="img" aria-label="Photo of a glowing red transparent LED brick in front of a red and grey brick wall"></div>
  <h1 class="title"><span class="title-led">LED</span><span class="title-klemm">KLEMMBAU</span><span class="title-steine">STEINE</span></h1>
  <div class="feature feature-fit">
    <svg width="30" height="22" viewBox="0 0 30 22" fill="none" stroke="#e0202a" stroke-width="1.6"><rect x="2" y="8" width="26" height="12" rx="1"/><rect x="6" y="3" width="6" height="5"/><rect x="18" y="3" width="6" height="5"/></svg>
    <span class="feature-label">EASY APPLY TO</span>
    <span class="partner-name">PINDO</span>
    <span class="partner-more">AND MORE</span>
  </div>
  <div class="feature feature-charge">
    <svg width="34" height="30" viewBox="0 0 34 30" fill="none" stroke="#ffffff" stroke-width="1.4"><circle cx="23" cy="10" r="8" stroke-dasharray="3 2"/><path d="M24 5 L20 11 H25 L22 16" stroke="#e0202a"/><path d="M3 16 L14 24 M6 13 L17 21"/></svg>
    <span class="feature-label">EASY USB<br>CHARGER</span>
  </div>
  <p class="set-id">S-58471<br>BASIC TRANSPARENT</p>
  <div class="swatches"><span class="swatch swatch-white"></span><span class="swatch swatch-red"></span><span class="swatch swatch-blue"></span><span class="swatch swatch-yellow"></span><span class="swatch swatch-green"></span></div>
  <div class="logo-block"><span class="logo-square"></span><span class="logo-name">FERNWALD<br>TOYHAUS</span></div>
</section>

<!-- Dieline: back panel -->
<div class="tuck-flap"></div>
<section class="back-panel" aria-label="Rückseite"></section>
<p class="back-title">LED KLEMMBAUSTEINE</p>
<p class="part-label part-label-cable inverted">USB CABLE</p>
<p class="part-label part-label-power inverted">RECHARGEABLE POWER BRICK</p>
<div class="part-box part-box-cable" role="img" aria-label="Photo of a coiled black USB cable"></div>
<div class="part-box part-box-power" role="img" aria-label="Photo of a black rechargeable power brick"></div>
<span class="count inverted" style="left:568px;top:1253px">x1</span>
<span class="count inverted" style="left:700px;top:1253px">x1</span>

<span class="count inverted" style="left:525px;top:1306px">x2</span>
<span class="brick brick-red" role="img" aria-label="Photo of a small red LED brick" style="left:543px;top:1302px;width:20px;height:20px"></span>
<span class="count inverted" style="left:525px;top:1338px">x2</span>
<span class="brick brick-blue" role="img" aria-label="Photo of a small blue LED brick" style="left:543px;top:1334px;width:20px;height:20px"></span>

<span class="count inverted" style="left:584px;top:1308px">x1</span>
<span class="brick brick-red" role="img" aria-label="Photo of a red 2x2 LED brick" style="left:601px;top:1300px;width:29px;height:24px"></span>
<span class="count inverted" style="left:584px;top:1346px">x1</span>
<span class="brick brick-blue" role="img" aria-label="Photo of a blue 2x2 LED brick" style="left:601px;top:1338px;width:29px;height:24px"></span>
<span class="count inverted" style="left:584px;top:1384px">x1</span>
<span class="brick brick-green" role="img" aria-label="Photo of a green 2x2 LED brick" style="left:601px;top:1376px;width:29px;height:24px"></span>
<span class="count inverted" style="left:584px;top:1422px">x1</span>
<span class="brick brick-yellow" role="img" aria-label="Photo of a yellow 2x2 LED brick" style="left:601px;top:1414px;width:29px;height:24px"></span>
<span class="count inverted" style="left:584px;top:1460px">x2</span>
<span class="brick brick-white" role="img" aria-label="Photo of a white 2x2 LED brick" style="left:601px;top:1452px;width:29px;height:24px"></span>

<span class="count inverted" style="left:659px;top:1308px">x4</span>
<span class="brick brick-green" role="img" aria-label="Photo of a green 2x3 LED brick" style="left:677px;top:1300px;width:37px;height:26px"></span>
<span class="count inverted" style="left:659px;top:1346px">x4</span>
<span class="brick brick-yellow" role="img" aria-label="Photo of a yellow 2x3 LED brick" style="left:677px;top:1338px;width:37px;height:26px"></span>
<span class="count inverted" style="left:659px;top:1384px">x4</span>
<span class="brick brick-blue" role="img" aria-label="Photo of a blue 2x3 LED brick" style="left:677px;top:1376px;width:37px;height:26px"></span>
<span class="count inverted" style="left:659px;top:1422px">x4</span>
<span class="brick brick-red" role="img" aria-label="Photo of a red 2x3 LED brick" style="left:677px;top:1414px;width:37px;height:26px"></span>
<span class="count inverted" style="left:659px;top:1460px">x4</span>
<span class="brick brick-white" role="img" aria-label="Photo of a white 2x3 LED brick" style="left:677px;top:1452px;width:37px;height:26px"></span>

<span class="count inverted" style="left:746px;top:1308px">x4</span>
<span class="brick brick-green" role="img" aria-label="Photo of a green 2x4 LED brick" style="left:764px;top:1298px;width:53px;height:30px"></span>
<span class="count inverted" style="left:746px;top:1346px">x4</span>
<span class="brick brick-yellow" role="img" aria-label="Photo of a yellow 2x4 LED brick" style="left:764px;top:1336px;width:53px;height:30px"></span>
<span class="count inverted" style="left:746px;top:1384px">x4</span>
<span class="brick brick-blue" role="img" aria-label="Photo of a blue 2x4 LED brick" style="left:764px;top:1374px;width:53px;height:30px"></span>
<span class="count inverted" style="left:746px;top:1422px">x4</span>
<span class="brick brick-red" role="img" aria-label="Photo of a red 2x4 LED brick" style="left:764px;top:1412px;width:53px;height:30px"></span>
<span class="count inverted" style="left:746px;top:1460px">x4</span>
<span class="brick brick-white" role="img" aria-label="Photo of a white 2x4 LED brick" style="left:764px;top:1450px;width:53px;height:30px"></span>

<p class="content-bar inverted">CONTENT</p>
<div class="mini-logo inverted" style="left:414px;top:1490px"><span class="logo-square"></span><span>FERNWALD<br>TOYHAUS</span></div>

<!-- Dieline: side panel -->
<div class="side-panel"></div>
<p class="side-title inverted">LED KLEMMBAUSTEINE</p>
<div class="side-brick" role="img" aria-label="Photo of a glowing red LED brick"></div>
<div class="mini-logo inverted" style="left:414px;top:1597px"><span class="logo-square"></span><span>FERNWALD<br>TOYHAUS</span></div>

<!-- Dieline: front with side flaps -->
<div class="front-flaps"></div>
<section class="front-face front-dieline" aria-label="Verpackungsfront im Stanzbogen">
  <div class="front-photo" role="img" aria-label="Photo of a glowing red transparent LED brick in front of a red and grey brick wall"></div>
  <p class="title"><span class="title-led">LED</span><span class="title-klemm">KLEMMBAU</span><span class="title-steine">STEINE</span></p>
  <div class="feature feature-fit">
    <svg width="30" height="22" viewBox="0 0 30 22" fill="none" stroke="#e0202a" stroke-width="1.6"><rect x="2" y="8" width="26" height="12" rx="1"/><rect x="6" y="3" width="6" height="5"/><rect x="18" y="3" width="6" height="5"/></svg>
    <span class="feature-label">EASY APPLY TO</span>
    <span class="partner-name">PINDO</span>
    <span class="partner-more">AND MORE</span>
  </div>
  <div class="feature feature-charge">
    <svg width="34" height="30" viewBox="0 0 34 30" fill="none" stroke="#ffffff" stroke-width="1.4"><circle cx="23" cy="10" r="8" stroke-dasharray="3 2"/><path d="M24 5 L20 11 H25 L22 16" stroke="#e0202a"/><path d="M3 16 L14 24 M6 13 L17 21"/></svg>
    <span class="feature-label">EASY USB<br>CHARGER</span>
  </div>
  <p class="set-id">S-58471<br>BASIC TRANSPARENT</p>
  <div class="swatches"><span class="swatch swatch-white"></span><span class="swatch swatch-red"></span><span class="swatch swatch-blue"></span><span class="swatch swatch-yellow"></span><span class="swatch swatch-green"></span></div>
  <div class="logo-block"><span class="logo-square"></span><span class="logo-name">FERNWALD<br>TOYHAUS</span></div>
</section>

<!-- Dieline: bottom panel with legal info -->
<div class="bottom-panel"></div>
<p class="legal-id"><strong>S-58471</strong><br>made in China</p>
<svg class="age-icon" width="22" height="22" viewBox="0 0 22 22" fill="none"><circle cx="11" cy="11" r="9.5" stroke="#e0202a" stroke-width="2"/><line x1="4" y1="18" x2="18" y2="4" stroke="#e0202a" stroke-width="2"/></svg>
<p class="warning warning-a">WARNING: Choking hazard, small parts. Not for children under 3 years. Strangulation hazard due to the cable. Keep away from young children.</p>
<p class="warning warning-b">ATTENTION: Small parts may be swallowed. Not suitable for children under 3 years. Risk of strangulation from the cable. Adult supervision advised.</p>
<p class="mark-ce">CE</p>
<svg class="mark-icons" width="46" height="18" viewBox="0 0 46 18" fill="none" stroke="#ffffff" stroke-width="1.3"><path d="M5 4 L9 4 L11 8 M13 13 L9 15 L4 12 M3 8 L5 4"/><circle cx="36" cy="9" r="7.5"/><path d="M32 10 L36 6 L40 10"/></svg>
<div class="importer">
  <p>Imported to DE, A and CH by</p>
  <div class="mini-logo"><span class="logo-square"></span><span>FERNWALD TOYHAUS</span></div>
  <p>Musterweg 12, 00000 Beispielstadt</p>
  <p>Imported to all other EU countries by</p>
  <span class="partner-chip"></span>
  <p>Glimo Kuv Europe, Beispielstraat 4</p>
  <p>Imported to all non EU countries by</p>
  <span class="partner-chip"></span>
  <p>Tallow Toy Co., Sample Lane 8</p>
</div>

</body>
</html>
```